Business card for concrete contractor
T.W. Concrete Construction, LLC
Business card for concrete contractor - Construction
Creative Brief
Traditional
Dale Fenwick
President
4170 E Marlin Ave., 2B Brenwick, IL 60921
dale@twconcrete-example.com
www.twconcrete-example.com
Licensed Bonded and Insured

```html
<!DOCTYPE html>
<html lang="en">
<head>
<meta charset="utf-8">
<title>T.W. Concrete Construction, LLC — Business Card</title>
<link rel="stylesheet" href="https://fonts.googleapis.com/css2?family=Lato:wght@400;700&display=swap">
<style>
  :root {
    --page: #ecebe8;
    --frame: #2f8fcb;
    --card: #ffffff;
    --ink-blue: #1f6d9f;
    --ink-green: #6aa238;
    --ink-grey: #6f7378;
    --rule: #9aa0a6;
  }
  * { box-sizing: border-box; margin: 0; padding: 0; }
  html, body {
    width: 1200px; height: 914px; overflow: hidden;
    background: var(--page);
  }
  body {
    display: flex; align-items: center; justify-content: center;
    font-family: "Lato", sans-serif;
  }
  .business-card {
    width: 1000px; height: 572px;
    background: var(--frame);
    padding: 24px;
    box-shadow: 0 10px 30px rgba(0,0,0,0.15);
  }
  .card-face {
    width: 100%; height: 100%;
    background: var(--card);
    position: relative;
  }
  .brand {
    position: absolute; top: 96px; left: 0; right: 0;
    text-align: center;
  }
  .brand-name {
    font-weight: 700; font-size: 44px; letter-spacing: 0.5px;
    color: var(--ink-blue); line-height: 1.15;
  }
  .tagline {
    margin: 16px auto 0;
    width: 520px;
    padding-top: 10px;
    border-top: 2px solid var(--ink-grey);
    font-size: 17px; letter-spacing: 3px; text-transform: uppercase;
    color: var(--ink-grey);
  }
  .details {
    position: absolute; top: 300px; left: 0; right: 0;
    display: grid; grid-template-columns: 1fr 1px 1fr;
    column-gap: 28px; align-items: start;
  }
  .identity { text-align: right; }
  .person-name {
    font-size: 20px; font-weight: 700; color: var(--ink-green);
  }
  .person-title {
    font-size: 14px; color: var(--ink-grey); margin-top: 4px;
    letter-spacing: 1px; text-transform: uppercase;
  }
  .address {
    font-style: normal;
    font-size: 15px; line-height: 1.6;
    color: var(--ink-grey); margin-top: 18px;
  }
  .divider { background: var(--rule); height: 140px; margin-top: 30px; }
  .contact-list {
    list-style: none; padding-top: 52px;
    font-size: 15px; color: var(--ink-grey);
  }
  .contact-list li {
    display: flex; align-items: center; gap: 10px; margin-bottom: 10px;
  }
  .contact-icon { width: 18px; height: 18px; flex: none; }
</style>
</head>
<body>
  <div class="business-card">
    <div class="card-face">
      <header class="brand">
        <p class="brand-name">T.W. Concrete Construction, LLC</p>
        <p class="tagline">Licensed, Bonded and Insured</p>
      </header>

      <section class="details">
        <div class="identity">
          <p class="person-name">Dale Fenwick</p>
          <p class="person-title">President</p>
          <address class="address">
            4170 E Marlin Ave., 2B<br>
            Brenwick, IL 60921
          </address>
        </div>
        <div class="divider"></div>
        <ul class="contact-list">
          <li>
            <svg class="contact-icon" viewBox="0 0 18 18" aria-hidden="true">
              <circle cx="9" cy="9" r="9" fill="var(--ink-blue)"/>
              <path d="M6 4.5l2 2-1 1.3c.6 1.3 1.6 2.3 2.9 2.9l1.3-1 2 2-1.2 1.5C8.7 13 5 9.3 4.8 5.7z" fill="#fff"/>
            </svg>
            (555) 014-2870
          </li>
          <li>
            <svg class="contact-icon" viewBox="0 0 18 18" aria-hidden="true">
              <circle cx="9" cy="9" r="9" fill="var(--ink-blue)"/>
              <rect x="4.5" y="6" width="9" height="6.5" fill="none" stroke="#fff" stroke-width="1.2"/>
              <path d="M4.5 6l4.5 3.6L13.5 6" fill="none" stroke="#fff" stroke-width="1.2"/>
            </svg>
            dale@twconcrete-example.com
          </li>
          <li>
            <svg class="contact-icon" viewBox="0 0 18 18" aria-hidden="true">
              <circle cx="9" cy="9" r="9" fill="var(--ink-blue)"/>
              <circle cx="9" cy="9" r="4.5" fill="none" stroke="#fff" stroke-width="1.1"/>
              <path d="M4.5 9h9M9 4.5c-2 2.5-2 6.5 0 9M9 4.5c2 2.5 2 6.5 0 9" fill="none" stroke="#fff" stroke-width="1"/>
            </svg>
            www.twconcrete-example.com
          </li>
        </ul>
      </section>
    </div>
  </div>
</body>
</html>
```